Kestrel Ridgeway LLC stationery, business card and web page design.

i need a full set of stationery designed using the name "Kestrel Ridgeway LLC" with a tag line "construction consulting services". using the uploaded monkey icon as the logo.

i like the colors orange, green and black in general but im not limited to that. the company offers consulting services to various types of construction businesses.

Target Market(s)

i travel around the country in a 4x4 camper offering consulting services and technical training short term and long to various types of construction companies.

Industry/Entity Type

Construction Company

Contact Information for Business Card

Martin Hale
m.hale@kestrelridgeway.example
2475 Birchfield Rd
Bohemia, NY 11716
555 314 0627

list these services on the card.

Business Consulting
Capital Investments
Marketing Implementations
Technical Training

Number of Pages Required

1 page

Colors

Designer to choose colors to be used in the design.

Requirements
Must have
• company info and use of the monkey icon i provided.
Nice to have
• a fun but professional design
Should not have
• the color red

```html
<!DOCTYPE html>
<html lang="en">
<head>
<meta charset="utf-8">
<title>Kestrel Ridgeway LLC — Stationery Set</title>
<link rel="stylesheet" href="https://fonts.googleapis.com/css2?family=Oswald:wght@400;500&family=Questrial&family=Lato:wght@300;400&display=swap">
<style>
  :root{
    --orange:#e8602f;
    --ink:#141414;
    --paper:#ffffff;
    --table:#ece9e6;
    --body-grey:#555555;
  }
  *{box-sizing:border-box;margin:0;padding:0}
  html,body{width:1200px;height:1034px;overflow:hidden;background:var(--table)}
  .canvas{position:relative;width:1200px;height:1034px}
  .piece{position:absolute;overflow:hidden}
  .brand{font-family:"Oswald",sans-serif;font-weight:400;letter-spacing:1.5px;text-transform:uppercase;white-space:nowrap}
  .contact{font-family:"Questrial",sans-serif;white-space:nowrap}
  .label{color:var(--orange);font-weight:700}
  .edge-band{position:absolute;left:0;bottom:0;width:100%;height:10px;display:block}

  /* Letterhead */
  .letterhead{left:66px;top:77px;width:498px;height:643px;background:var(--paper)}
  .letterhead .brand-mark{position:absolute;left:42px;top:30px;width:56px;height:56px;border-radius:50%;background:var(--ink)}
  .letterhead .brand{position:absolute;left:132px;top:40px;font-size:21px;color:var(--orange)}
  .letter-body{position:absolute;left:46px;top:136px;width:406px;font-family:"Lato",sans-serif}
  .greeting{font-size:11.5px;font-weight:300;color:#333;margin-bottom:8px}
  .letter-body p.para{font-size:6.2px;line-height:9.8px;color:var(--body-grey);margin-bottom:7px}
  .letter-body p.para.gap{margin-bottom:20px}
  .sign-off{position:absolute;left:46px;top:472px;font-family:"Lato",sans-serif}
  .sign-off .regards{font-size:11.5px;font-weight:300;color:#333}
  .sign-off .signer{font-size:7px;color:#444;margin-top:1px}
  .sign-rule{position:absolute;left:48px;top:508px;width:73px;height:1px;background:#444}
  .signature{position:absolute;left:57px;top:522px;width:72px;height:34px;background:linear-gradient(90deg,#e9e9e9,#d4d4d4)}
  .letterhead .contact-block{position:absolute;left:0;top:590px;width:100%;text-align:center;font-size:9.4px;line-height:13px;color:#333}

  /* Envelope */
  .envelope{left:618px;top:77px;width:522px;height:337px;background:var(--paper);overflow:visible}
  .envelope .flap{position:absolute;left:0;top:0;width:522px;height:60px;display:block}
  .envelope .brand-mark{position:absolute;left:251px;top:13px;width:20px;height:20px;border-radius:50%;background:var(--ink)}
  .envelope .brand{position:absolute;left:0;top:180px;width:100%;text-align:center;font-size:25px;color:var(--ink)}

  /* Large orange card */
  .card-back{left:618px;top:444px;width:522px;height:276px;background:var(--orange)}
  .card-back .brand{position:absolute;left:0;top:122px;width:100%;text-align:center;font-size:25px;color:var(--paper)}
  .card-back .contact-block{position:absolute;left:0;top:229px;width:100%;text-align:center;font-size:10.4px;line-height:15px;color:#fff}
  .card-back .label{color:var(--ink)}

  /* Business card front (white) */
  .card-front{left:205px;top:762px;width:360px;height:206px;background:var(--paper)}
  .card-front .person{position:absolute;right:209px;top:86px;text-align:right}
  .card-front .person-name{font-family:"Oswald",sans-serif;font-size:18px;letter-spacing:1px;text-transform:uppercase;color:var(--ink);line-height:22px;white-space:nowrap}
  .card-front .person-role{font-family:"Questrial",sans-serif;font-size:10px;letter-spacing:.5px;text-transform:uppercase;color:var(--orange);margin-top:1px}
  .card-front .divider{position:absolute;left:165px;top:84px;width:1px;height:44px;background:var(--ink)}
  .card-front .contact-block{position:absolute;left:175px;top:84px;font-size:7.6px;line-height:10.6px;color:var(--ink)}
  .card-front .services{position:absolute;left:0;top:150px;width:100%;text-align:center;font-family:"Questrial",sans-serif;font-size:7.2px;line-height:11px;color:var(--ink);letter-spacing:.3px}
  .card-front .services .dot{color:var(--orange);padding:0 4px}

  /* Small orange card */
  .card-brand{left:626px;top:762px;width:361px;height:206px;background:var(--orange)}
  .card-brand .brand-mark{position:absolute;left:150px;top:50px;width:60px;height:60px;border-radius:50%;background:var(--ink)}
  .card-brand .brand{position:absolute;left:0;top:122px;width:100%;text-align:center;font-size:18px;color:var(--paper)}
  .card-brand .tagline{position:absolute;left:0;top:156px;width:100%;text-align:center;font-family:"Questrial",sans-serif;font-size:8px;letter-spacing:1.5px;text-transform:uppercase;color:var(--ink)}
  .card-brand .site{position:absolute;left:0;top:183px;width:100%;text-align:center;font-size:7.4px;color:#fff}
</style>
</head>
<body>
<main class="canvas">

  <section class="piece letterhead" aria-label="Letterhead">
    <span class="brand-mark"></span>
    <div class="brand">Kestrel Ridgeway LLC</div>

    <div class="letter-body">
      <p class="greeting">Hello Peter,</p>
      <p class="para">Thank you for meeting with us on site last week. This letter confirms the scope we discussed for the coming season, including a review of your current crew schedules, material ordering, equipment use and safety training needs across all three of your active projects. We will share a short written plan before the work begins so that your team knows what to expect, who to contact and how each visit will run from start to finish.</p>
      <p class="para gap">Our first visit will cover the office side of the business: bids, cash flow, job costing and the tools your managers use each day. The second visit moves to the field, where we will walk active sites with your foremen, look at how tasks are planned and handed over, and note the places where time or material is lost. After both visits we will meet again to agree on priorities, set clear targets for the next quarter and choose the training sessions that fit your people best. We will also review how change orders are logged, how subcontractor invoices are checked against progress, and how often site reports reach the office. Any quick wins we find along the way will be shared with you at once rather than held for the final report.</p>
      <p class="para">Training can be held at your yard or on a live job. Each session runs for half a day and mixes short talks with hands-on practice, so new hires and senior staff can learn side by side and put the ideas to use the same week. Each attendee receives a short printed guide to keep in the site office, and we can return a month later to check progress, answer questions and adjust the plan where needed.</p>
      <p class="para gap">Our first visit will cover the office side of the business: bids, cash flow, job costing and the tools your managers use each day. The second visit moves to the field, where we will walk active sites with your foremen, look at how tasks are planned and handed over, and note the places where time or material is lost. After both visits we will meet again to agree on priorities, set clear targets for the next quarter and choose the training sessions that fit your people best. We will also review how change orders are logged, how subcontractor invoices are checked against progress, and how often site reports reach the office. Any quick wins we find along the way will be shared with you at once rather than held for the final report.</p>
      <p class="para">Please let me know which dates suit you, and I will plan my route to reach your area in good time. I look forward to working with your team again and to seeing the progress on your current sites.</p>
    </div>

    <div class="sign-off">
      <p class="regards">Regards,</p>
      <p class="signer">Lena Brooks</p>
    </div>
    <span class="sign-rule"></span>
    <div class="signature" role="img" aria-label="Handwritten signature"></div>

    <div class="contact contact-block">
      <div><span class="label">A:</span> 2475 Birchfield Rd, Bohemia, NY 11716</div>
      <div><span class="label">P:</span> 555 314 0627 <span class="label">E:</span> m.hale@kestrelridgeway.example <span class="label">W:</span> www.kestrelridgeway.example</div>
    </div>

    <svg class="edge-band" viewBox="0 0 498 10" preserveAspectRatio="none" aria-hidden="true">
      <rect width="498" height="10" fill="var(--orange)"/>
      <polygon points="97,10 106,0 415,0 424,10" fill="#fff"/>
      <polygon points="100,10 108,1 413,1 421,10" fill="var(--ink)"/>
    </svg>
  </section>

  <section class="piece envelope" aria-label="Envelope">
    <svg class="flap" viewBox="0 0 522 60" aria-hidden="true">
      <polygon points="0,60 22,0 478,0 522,60" fill="var(--orange)"/>
    </svg>
    <span class="brand-mark"></span>
    <div class="brand">Kestrel Ridgeway LLC</div>
  </section>

  <section class="piece card-back" aria-label="Compliment card">
    <div class="brand">Kestrel Ridgeway LLC</div>
    <div class="contact contact-block">
      <div><span class="label">A:</span> 2475 Birchfield Rd, Bohemia, NY 11716</div>
      <div><span class="label">P:</span> 555 314 0627 <span class="label">E:</span> m.hale@kestrelridgeway.example <span class="label">W:</span> www.kestrelridgeway.example</div>
    </div>
    <svg class="edge-band" viewBox="0 0 522 10" preserveAspectRatio="none" aria-hidden="true">
      <rect width="522" height="10" fill="#fff"/>
      <polygon points="90,10 99,0 432,0 441,10" fill="var(--orange)"/>
      <polygon points="93,10 101,1 430,1 438,10" fill="var(--ink)"/>
    </svg>
  </section>

  <section class="piece card-front" aria-label="Business card front">
    <div class="person">
      <div class="person-name">Martin Hale</div>
      <div class="person-role">Director</div>
    </div>
    <span class="divider"></span>
    <div class="contact contact-block">
      <div>2475 Birchfield Rd</div>
      <div>Bohemia, NY 11716</div>
      <div><span class="label">P:</span> 555 314 0627</div>
      <div><span class="label">E:</span> m.hale@kestrelridgeway.example</div>
    </div>
    <div class="services">
      <div>Business Consulting<span class="dot">•</span>Capital Investments</div>
      <div>Marketing Implementations<span class="dot">•</span>Technical Training</div>
    </div>
    <svg class="edge-band" viewBox="0 0 360 10" preserveAspectRatio="none" aria-hidden="true">
      <rect width="360" height="10" fill="var(--orange)"/>
      <polygon points="63,10 72,0 292,0 301,10" fill="#fff"/>
      <polygon points="66,10 74,1 290,1 298,10" fill="var(--ink)"/>
    </svg>
  </section>

  <section class="piece card-brand" aria-label="Business card brand side">
    <span class="brand-mark"></span>
    <div class="brand">Kestrel Ridgeway LLC</div>
    <div class="tagline">Construction Consulting Services</div>
    <div class="contact site">www.kestrelridgeway.example</div>
    <svg class="edge-band" viewBox="0 0 361 10" preserveAspectRatio="none" aria-hidden="true">
      <rect width="361" height="10" fill="#fff"/>
      <polygon points="61,10 70,0 297,0 306,10" fill="var(--orange)"/>
      <polygon points="64,10 72,1 295,1 303,10" fill="var(--ink)"/>
    </svg>
  </section>

</main>
</body>
</html>
```